KBMR new business card design

We need a business card design for our established business which is Australia wide however based in Melbourne. We are a young team of Financial Planners who specialize in Insurance and Basic super advice for people like us.

We are people who help our clients get things done in a timely and cost effective manner whilst having a good time and a laugh along the way.

We would like this to have a consistent feel with our new e-brochure which i have attached from a color and font perspective.

Industry/Entity Type

Business

Requirements
Must have
• We do not need specific address details rather just the states we are in:

VIC/NSW/QLD/TAS
Nice to have
• Curved edge to mate the brochure

```html
<!DOCTYPE html>
<html lang="en">
<head>
<meta charset="utf-8">
<title>KBMR Planning – Business Card</title>
<link rel="stylesheet" href="https://fonts.googleapis.com/css2?family=Montserrat:wght@400;500;600;700&display=swap">
<style>
  :root {
    --ink: #1e1e1e;
    --lime: #6cc04a;
    --white: #ffffff;
    --backdrop: #d9d9d9;
    --card-w: 660px;
    --card-h: 378px;
    --curve: 56px;
  }
  * { box-sizing: border-box; margin: 0; padding: 0; }
  html, body {
    width: 1200px;
    height: 900px;
    overflow: hidden;
  }
  body {
    background: var(--backdrop);
    font-family: "Montserrat", Arial, sans-serif;
    display: flex;
    flex-direction: column;
    align-items: center;
    justify-content: center;
    gap: 44px;
  }
  .card {
    position: relative;
    width: var(--card-w);
    height: var(--card-h);
    border-radius: var(--curve) 0 var(--curve) 0;
    overflow: hidden;
    box-shadow: 0 6px 18px rgba(0,0,0,0.18);
  }

  /* Reverse side */
  .card--reverse { background: var(--ink); }
  .card--reverse::after {
    content: "";
    position: absolute;
    right: 0; top: 0; bottom: 0;
    width: 14px;
    background: var(--lime);
    border-radius: 0 0 var(--curve) 0;
  }
  .tagline {
    position: absolute;
    left: 60px;
    top: 150px;
    color: var(--lime);
    font-weight: 500;
    font-size: 19px;
    letter-spacing: 0.22em;
    line-height: 1.45;
    text-transform: uppercase;
  }
  .brand {
    display: flex;
    align-items: center;
    gap: 12px;
    color: var(--white);
    font-weight: 700;
  }
  .brand__square {
    background: var(--lime);
    border-radius: 8px;
    flex: none;
  }
  .card--reverse .brand {
    position: absolute;
    right: 56px;
    top: 110px;
    font-size: 32px;
  }
  .card--reverse .brand__square { width: 52px; height: 52px; }

  /* Front side */
  .card--front {
    display: grid;
    grid-template-columns: 300px 1fr;
    background: var(--ink);
  }
  .identity {
    display: flex;
    align-items: center;
    justify-content: center;
  }
  .card--front .brand {
    flex-direction: column;
    gap: 18px;
    font-size: 46px;
    letter-spacing: 0.02em;
  }
  .card--front .brand__square {
    width: 120px;
    height: 120px;
    border-radius: 18px;
  }
  .details {
    background: var(--lime);
    border-radius: 0 0 var(--curve) 0;
    display: flex;
    flex-direction: column;
    padding-top: 38px;
  }
  .nameplate {
    background: var(--ink);
    padding: 14px 28px 12px;
  }
  .nameplate__name {
    color: var(--white);
    font-weight: 500;
    font-size: 22px;
    letter-spacing: 0.14em;
    text-transform: uppercase;
  }
  .nameplate__role {
    color: var(--lime);
    font-size: 15px;
    letter-spacing: 0.08em;
    margin-top: 2px;
  }
  .regions {
    margin: 40px 28px 0;
    color: var(--ink);
    font-size: 14px;
    font-weight: 500;
    letter-spacing: 0.1em;
    line-height: 1.45;
    text-transform: uppercase;
  }
  .contacts {
    list-style: none;
    margin: 18px 28px 0;
    color: var(--ink);
    font-size: 15px;
    font-weight: 500;
    letter-spacing: 0.05em;
  }
  .contacts__item {
    display: flex;
    align-items: center;
    gap: 10px;
    line-height: 1.7;
  }
  .contacts__icon {
    width: 16px;
    height: 16px;
    flex: none;
  }
</style>
</head>
<body>

  <section class="card card--reverse" aria-label="Card reverse">
    <p class="tagline">Clear advice,<br>confident tomorrow</p>
    <div class="brand">
      <span class="brand__square"></span>
      <span class="brand__name">KBMR</span>
    </div>
  </section>

  <section class="card card--front" aria-label="Card front">
    <div class="identity">
      <div class="brand">
        <span class="brand__square"></span>
        <span class="brand__name">KBMR</span>
      </div>
    </div>

    <div class="details">
      <div class="nameplate">
        <p class="nameplate__name">Daniel Harper</p>
        <p class="nameplate__role">President</p>
      </div>

      <p class="regions">VIC / NSW / QLD / TAS<br>Australia wide</p>

      <ul class="contacts">
        <li class="contacts__item">
          <svg class="contacts__icon" viewBox="0 0 16 16" aria-hidden="true">
            <rect x="0.75" y="0.75" width="14.5" height="14.5" fill="none" stroke="#1e1e1e" stroke-width="1.5"/>
            <path d="M4.5 3.5 L6.5 3.5 L7 6 L5.8 7 C6.5 8.5 7.5 9.5 9 10.2 L10 9 L12.5 9.5 L12.5 11.5 C8 12 4 8 4.5 3.5 Z" fill="#1e1e1e"/>
          </svg>
          <span>1300 555 014</span>
        </li>
        <li class="contacts__item">
          <svg class="contacts__icon" viewBox="0 0 16 16" aria-hidden="true">
            <rect x="0.75" y="0.75" width="14.5" height="14.5" fill="none" stroke="#1e1e1e" stroke-width="1.5"/>
            <rect x="3.5" y="4.5" width="9" height="7" fill="none" stroke="#1e1e1e" stroke-width="1.2"/>
            <path d="M3.5 4.5 L8 8.5 L12.5 4.5" fill="none" stroke="#1e1e1e" stroke-width="1.2"/>
          </svg>
          <span>admin@kbmr.com.au</span>
        </li>
        <li class="contacts__item">
          <svg class="contacts__icon" viewBox="0 0 16 16" aria-hidden="true">
            <rect x="0.75" y="0.75" width="14.5" height="14.5" fill="none" stroke="#1e1e1e" stroke-width="1.5"/>
            <circle cx="8" cy="8" r="2" fill="none" stroke="#1e1e1e" stroke-width="1.2"/>
            <path d="M10 6 L10 9 C10 10.5 12 10.5 12 8.5 A4 4 0 1 0 10.5 11.2" fill="none" stroke="#1e1e1e" stroke-width="1.2"/>
          </svg>
          <span>www.kbmrplanning.com.au</span>
        </li>
      </ul>
    </div>
  </section>

</body>
</html>
```